TR Advisory Business Cards - High End AV / Low Voltage Company

We are low voltage AV company that specializes in high end clients on the residential side and larger businesses on the commercial side. We want something modern, tech looking but also something that is extremely professional looking. We have uploaded our logos and postcards we already have in the field. Along with a picture of one of our wrapped vans. Our website is at www.trvadvisory.example and our primary colors are the orange, green, grey and blue all military color finishes.

We are interesting in the slogans "Connecting You with Smarter Technology" or "Leading the Lowcountry in Tech"

Target Market(s)

We focus on 70% Commercial and 30% Residential Customers

Industry/Entity Type

Low Voltage, AV Company

Contact Information for Business Card

Name - Dorian Fairweather, Title - Owner, Office Phone - 555-714-3096, Mobile Phone - 555-802-4173, E-Mail - d@trvadvisory.example, Website: www.trvadvisory.example

Font styles to use
Sans Serif

Requirements
Must have
• Must have Name, Title, Work Phone & Mobile, Website and Logo.
Nice to have
• We want something that will impress our higher end clients with a great logo
Should not have
• Too traditional or plain.

```html
<!DOCTYPE html>
<html lang="en">
<head>
<meta charset="utf-8">
<title>TR Advisory Business Card</title>
<link rel="stylesheet" href="https://fonts.googleapis.com/css2?family=Montserrat:wght@500;600&family=Open+Sans:wght@400;700&display=swap">
<style>
  :root {
    --orange: #eb6434;
    --orange-light: #ee7a42;
    --white: #ffffff;
    --ink: #2f3a17;
    --canvas: #d3d4d6;
  }
  * { margin: 0; padding: 0; box-sizing: border-box; }
  html, body { width: 900px; height: 1200px; overflow: hidden; }
  body {
    position: relative;
    background: var(--canvas);
    font-family: "Open Sans", Arial, sans-serif;
  }
  .card {
    position: absolute;
    left: 136px;
    width: 630px;
    height: 358px;
    border-radius: 14px;
    overflow: hidden;
  }
  .card-front {
    top: 215px;
    background: linear-gradient(100deg, var(--orange) 0%, var(--orange-light) 100%);
    color: var(--white);
  }
  .card-back {
    top: 628px;
    background: var(--white);
  }
  .brand-ring {
    position: absolute;
    border-radius: 50%;
  }
  .card-front .brand-ring {
    left: 215px; top: 62px; width: 200px; height: 200px;
    border: 7px solid var(--white);
  }
  .brand-name {
    position: absolute;
    text-align: center;
    font-family: "Montserrat", Arial, sans-serif;
    font-weight: 600;
    letter-spacing: 2px;
    line-height: 1;
    white-space: nowrap;
  }
  .card-front .brand-name {
    left: 0; width: 100%;
    top: 268px;
    font-size: 34px;
    color: var(--white);
  }
  .slogan {
    position: absolute;
    left: 0; top: 317px; width: 100%;
    display: flex; align-items: center; justify-content: center; gap: 8px;
    font-family: "Montserrat", Arial, sans-serif;
    font-weight: 600;
    font-size: 14.5px;
    line-height: 18px;
  }
  .slogan-rule { width: 56px; height: 12px; }
  .card-back .brand-ring {
    left: 391px; top: 34px; width: 110px; height: 110px;
    border: 5px solid var(--orange);
  }
  .card-back .brand-name {
    left: 346px; width: 200px;
    top: 155px;
    font-size: 20px;
    color: var(--orange);
  }
  .person { position: absolute; left: 55px; top: 174px; }
  .person-name { font-size: 27px; font-weight: 700; color: var(--ink); line-height: 1.2; }
  .person-title { font-size: 15px; color: var(--orange); letter-spacing: 1px; margin-top: 1px; }
  .contacts {
    position: absolute; left: 372px; top: 226px;
    list-style: none;
  }
  .contacts li {
    display: flex; align-items: center; gap: 7px;
    height: 25.5px;
    font-size: 15.5px; color: var(--ink); letter-spacing: 0.8px;
  }
  .contacts li.phone { letter-spacing: 2.6px; }
  .contacts svg { width: 14px; height: 14px; flex: none; fill: var(--orange); }
  .contacts svg.globe { fill: none; stroke: var(--orange); stroke-width: 2; }
</style>
</head>
<body>
  <section class="card card-front">
    <div class="brand-ring"></div>
    <div class="brand-name">TR Advisory</div>
    <div class="slogan">
      <svg class="slogan-rule" viewBox="0 0 56 12"><circle cx="5" cy="6" r="4" fill="#fff"/><rect x="5" y="5" width="51" height="2" fill="#fff"/></svg>
      <span>CONNECTING YOU WITH SMARTER TECHNOLOGY</span>
      <svg class="slogan-rule" viewBox="0 0 56 12"><rect x="0" y="5" width="51" height="2" fill="#fff"/><circle cx="51" cy="6" r="4" fill="#fff"/></svg>
    </div>
  </section>

  <section class="card card-back">
    <div class="brand-ring"></div>
    <div class="brand-name">TR Advisory</div>
    <div class="person">
      <div class="person-name">Dorian Fairweather</div>
      <div class="person-title">Owner</div>
    </div>
    <ul class="contacts">
      <li class="phone"><svg viewBox="0 0 24 24"><path d="M6.6 10.8a15 15 0 0 0 6.6 6.6l2.2-2.2c.3-.3.7-.4 1-.2 1.1.4 2.3.6 3.6.6.6 0 1 .4 1 1V20c0 .6-.4 1-1 1C10.6 21 3 13.4 3 4c0-.6.4-1 1-1h3.5c.6 0 1 .4 1 1 0 1.3.2 2.5.6 3.6.1.3 0 .7-.2 1z"/></svg>555-714-3096</li>
      <li class="phone"><svg viewBox="0 0 24 24"><path d="M7 1h10a2 2 0 0 1 2 2v18a2 2 0 0 1-2 2H7a2 2 0 0 1-2-2V3a2 2 0 0 1 2-2zm0 3v14h10V4zm5 15.5a1 1 0 1 0 0 2 1 1 0 0 0 0-2z"/></svg>555-802-4173</li>
      <li><svg viewBox="0 0 24 24"><path d="M2 5h20v2l-10 6L2 7zm0 4 10 6 10-6v10H2z"/></svg>d@trvadvisory.example</li>
      <li><svg class="globe" viewBox="0 0 24 24"><circle cx="12" cy="12" r="9"/><ellipse cx="12" cy="12" rx="4" ry="9"/><path d="M3 12h18"/></svg>www.trvadvisory.example</li>
    </ul>
  </section>
</body>
</html>
```